Just Listed and Just Sold Post Cards. I have attached copies of what I have had in the past for reference. I have a new company logo attached that needs to be used. Please also include website: www.marshwillowfinder.com
email. brendakowal@brendakowalrealty.com
phone 555-203-7748
Target Market(s)
home and land owners
Font styles to use
Sans Serif
Colors
0356a4
Requirements
Must have
- I need a South Gulf Cove Just Listed Card and a Just Sold Card
- Must have My name company name logo website email phone number
- back should read _______. on your block of South Gulf Cove has just SOLD at $________ on _____________________ similar to the one I have attached.
Nice to have
- I like how the attached postcards from before have the shaded picture on the back of the picture on the front. I like to have the aerial as one main photo and the photo with the boat as the other main photo.
- Integrate my Brenda Kowal logo with the KT Vista logo

```html
<!DOCTYPE html>
<html lang="en">
<head>
<meta charset="utf-8">
<title>Just Listed Postcard – Brenda Kowal</title>
<link href="https://fonts.googleapis.com/css2?family=Archivo+Black&family=Roboto+Condensed:wght@400;700&family=Roboto:wght@400;700&display=swap" rel="stylesheet">
<style>
  :root {
    --brand-blue: #0356a4;
    --navy: #0b2a6b;
    --band-light: #1656b0;
    --orange: #f0801e;
    --orange-dark: #c85f0a;
    --slate: #5d6a86;
    --white: #ffffff;
    --stage: #d3d3d3;
    --photo-top: #5f93c9;
    --photo-bottom: #2f5a86;
  }
  * { margin: 0; padding: 0; box-sizing: border-box; }
  html, body { width: 1200px; height: 505px; overflow: hidden; }
  body { background: var(--stage); position: relative; font-family: "Roboto", sans-serif; }

  .postcard {
    position: absolute; left: 324px; top: 41px;
    width: 551px; height: 423px; overflow: hidden;
  }
  .hero-photo {
    position: absolute; inset: 0;
    background: linear-gradient(180deg, var(--photo-top) 0%, var(--photo-bottom) 100%);
  }
  .logo-wedge { position: absolute; left: 186px; top: 0; }

  .logo-panel {
    position: absolute; left: 210px; top: 0; width: 125px; height: 116px;
    background: var(--white);
    display: flex; flex-direction: column; align-items: center; justify-content: center; gap: 13px;
  }
  .company-mark { display: flex; flex-direction: column; align-items: center; }
  .company-name {
    display: flex; align-items: center; gap: 5px;
    font-family: "Roboto Condensed", sans-serif; font-weight: 700;
    font-size: 16px; color: var(--slate); letter-spacing: .5px;
  }
  .company-name .square { width: 13px; height: 13px; background: var(--slate); }
  .company-tagline { font-family: "Roboto Condensed", sans-serif; font-size: 5.5px; color: var(--slate); letter-spacing: .6px; margin-top: 1px; }

  .agent-mark { display: flex; flex-direction: column; align-items: center; }
  .agent-name {
    display: flex; align-items: center; gap: 4px;
    font-family: "Roboto Condensed", sans-serif; font-weight: 700;
    font-size: 12px; color: var(--navy); letter-spacing: .3px;
  }
  .agent-name .circle { width: 11px; height: 11px; border-radius: 50%; background: var(--orange); }
  .agent-title { font-family: "Roboto Condensed", sans-serif; font-size: 5.5px; font-weight: 700; color: var(--orange); letter-spacing: .4px; }

  .headline-braces { position: absolute; left: 136px; top: 120px; }
  .headline {
    position: absolute; left: 160px; top: 133px; width: 228px;
    text-align: center; font-family: "Archivo Black", sans-serif;
    color: var(--white); font-size: 58px; line-height: 58px;
    text-shadow: 0 2px 6px rgba(0,0,0,.25);
  }

  .contact-band {
    position: absolute; left: 0; top: 373px; width: 551px; height: 50px;
    background: var(--navy);
  }
  .contact-band .web-email {
    position: absolute; left: 0; top: 0; width: 315px; height: 50px;
    background: linear-gradient(90deg, var(--brand-blue), var(--band-light));
  }
  .contact-band .contact-text {
    position: absolute; left: 88px; top: 0; width: 200px; height: 50px;
    display: flex; flex-direction: column; justify-content: center; align-items: center;
    font-family: "Roboto Condensed", sans-serif; font-weight: 700; color: var(--white);
    font-size: 13px; line-height: 18px; letter-spacing: .2px; white-space: nowrap;
  }

  .phone-tag {
    position: absolute; left: 338px; top: 353px; width: 197px; height: 29px;
    background: var(--orange);
    display: flex; align-items: center; justify-content: center; gap: 5px;
    font-family: "Roboto Condensed", sans-serif; font-weight: 700; color: var(--white);
  }
  .phone-tag .label { font-size: 15px; }
  .phone-tag .number { font-size: 24px; letter-spacing: .2px; }
  .phone-fold { position: absolute; left: 514px; top: 382px; }
</style>
</head>
<body>
  <main class="postcard">
    <div class="hero-photo" role="img" aria-label="Photo area: aerial view of a Gulf coast canal community blending into a canal scene with a fishing boat and docks"></div>

    <svg class="logo-wedge" width="24" height="116" viewBox="0 0 24 116" aria-hidden="true">
      <polygon points="2,0 24,0 24,116" fill="#0b2a6b" opacity=".45"/>
    </svg>

    <div class="logo-panel">
      <div class="company-mark">
        <div class="company-name"><span class="square"></span>KT VISTA</div>
        <div class="company-tagline">HARLOW-AINSLEY REALTY</div>
      </div>
      <div class="agent-mark">
        <div class="agent-name"><span class="circle"></span>BRENDA KOWAL</div>
        <div class="agent-title">BROKER ASSOCIATE</div>
      </div>
    </div>

    <svg class="headline-braces" width="276" height="162" viewBox="0 0 276 162" aria-hidden="true">
      <path d="M24 2 C10 2 12 12 12 36 C12 64 12 74 2 81 C12 88 12 98 12 126 C12 150 10 160 24 160"
            fill="none" stroke="#fff" stroke-width="2.5"/>
      <path d="M250 2 C264 2 262 12 262 36 C262 64 262 74 274 81 C262 88 262 98 262 126 C262 150 264 160 250 160"
            fill="none" stroke="#fff" stroke-width="2.5"/>
    </svg>
    <h1 class="headline">Just<br>Listed</h1>

    <footer class="contact-band">
      <div class="web-email"></div>
      <div class="contact-text">
        <span class="website">www.marshwillowfinder.com</span>
        <span class="email">brendakowal@brendakowalrealty.com</span>
      </div>
    </footer>

    <div class="phone-tag"><span class="label">Phone:</span><span class="number">555-203-7748</span></div>
    <svg class="phone-fold" width="21" height="25" viewBox="0 0 21 25" aria-hidden="true">
      <polygon points="0,0 21,0 21,25" fill="var(--orange-dark)"/>
    </svg>
  </main>
</body>
</html>
```